IT Company looking to market towards Dental Offices

I am looking for a full-color design. Using my existing logo. Must have High Res stock photos. The brochure needs to be full page edge to edge design single fold pamphlet style. Content provided. Please see the website in attached Word Doc for more content.

```html
<!DOCTYPE html>
<html lang="en">
<head>
<meta charset="utf-8">
<title>Byte Harbor – Dental Services Brochure</title>
<link rel="stylesheet" href="https://fonts.googleapis.com/css2?family=Montserrat:wght@400;600;700;800&display=swap">
<style>
  :root {
    --canvas: #e8e9eb;
    --paper: #f3f4f6;
    --paper-grey: #c9cbcf;
    --navy: #0d2a7a;
    --royal: #1d47b3;
    --sky: #6fb6ff;
    --ribbon: #2f7be0;
    --ink-dark: #1e1f22;
    --ink-soft: #4a4d55;
    --white: #ffffff;
  }
  * { margin: 0; padding: 0; box-sizing: border-box; }
  html, body { width: 705px; height: 1200px; overflow: hidden; }
  body {
    background: var(--canvas);
    font-family: "Montserrat", Arial, sans-serif;
    position: relative;
  }
  .sheet { position: absolute; display: block; filter: drop-shadow(0 6px 10px rgba(0,0,0,.18)); }
  .front-cover-sheet { left: 160px; top: 50px; width: 386px; height: 500px; }
  .open-spread { position: absolute; left: 52px; top: 700px; width: 600px; height: 388px; display: flex; filter: drop-shadow(0 6px 10px rgba(0,0,0,.18)); }
  .open-spread svg { display: block; width: 300px; height: 388px; }
  .brand-name { font-weight: 700; fill: var(--navy); }
  .cover-heading { font-weight: 800; fill: var(--sky); letter-spacing: .3px; }
  .cover-copy { font-size: 7.1px; fill: var(--white); }
  .table-title { font-size: 7px; font-weight: 700; fill: var(--ink-dark); }
  .table-head { font-size: 6px; font-weight: 700; fill: var(--white); }
  .table-cell { font-size: 5.2px; fill: var(--ink-soft); }
  .ribbon-text { font-size: 5.6px; font-weight: 600; fill: var(--white); }
  .vault-heading { font-size: 13px; font-weight: 800; fill: var(--white); letter-spacing: .6px; }
  .vault-copy { font-size: 6px; fill: #e6e8ee; }
</style>
</head>
<body>

<svg width="0" height="0" style="position:absolute" aria-hidden="true">
  <defs>
    <linearGradient id="paper-fade" x1="0" y1="0" x2="1" y2="1">
      <stop offset="0" stop-color="#fbfbfc"/><stop offset="1" stop-color="#dfe1e5"/>
    </linearGradient>
    <linearGradient id="blue-band" x1="0" y1="0" x2="1" y2="1">
      <stop offset="0" stop-color="#2150c4"/><stop offset="1" stop-color="#0b2470"/>
    </linearGradient>
    <linearGradient id="room-tones" x1="0" y1="0" x2="0" y2="1">
      <stop offset="0" stop-color="#c9d8bd"/><stop offset=".45" stop-color="#dfe2e3"/><stop offset="1" stop-color="#8e949b"/>
    </linearGradient>
    <linearGradient id="desk-tones" x1="0" y1="0" x2="1" y2="1">
      <stop offset="0" stop-color="#d7e6c9"/><stop offset="1" stop-color="#b99a6a"/>
    </linearGradient>
    <linearGradient id="tools-tones" x1="0" y1="0" x2="1" y2="1">
      <stop offset="0" stop-color="#6b7078"/><stop offset="1" stop-color="#2b2e33"/>
    </linearGradient>
    <linearGradient id="vault-tones" x1="0" y1="0" x2="1" y2="0">
      <stop offset="0" stop-color="#b9bcc1"/><stop offset=".6" stop-color="#8d9096"/><stop offset="1" stop-color="#5a5d62"/>
    </linearGradient>
    <clipPath id="cover-clip"><rect width="386" height="500"/></clipPath>

    <symbol id="front-cover" viewBox="0 0 386 500">
      <g clip-path="url(#cover-clip)">
        <rect width="386" height="500" fill="url(#paper-fade)"/>
        <circle cx="300" cy="170" r="232" fill="url(#room-tones)" role="img" aria-label="Photo of a bright dental treatment room with a patient chair by the window"/>
        <path d="M0 500 L0 430 Q110 340 240 318 Q335 292 386 150 L386 500 Z" fill="url(#blue-band)"/>
        <path d="M0 428 Q110 338 240 316 Q335 290 386 148" fill="none" stroke="var(--sky)" stroke-width="4"/>
        <circle cx="298" cy="210" r="33" fill="url(#desk-tones)" stroke="var(--white)" stroke-width="3" role="img" aria-label="Photo of a dental office front desk"/>
        <circle cx="270" cy="280" r="33" fill="url(#tools-tones)" stroke="var(--white)" stroke-width="3" role="img" aria-label="Photo of dental instruments on a tray"/>
        <circle cx="40" cy="58" r="13" fill="var(--navy)"/>
        <text class="brand-name" x="60" y="64" font-size="17">Byte Harbor</text>
        <text class="cover-heading" x="92" y="380" font-size="17">DENTAL SERVICES</text>
        <text class="cover-copy" x="92" y="395">Byte Harbor offers proven expertise in dental practices. We have been serving</text>
        <text class="cover-copy" x="92" y="405">offices for years and specialize in dental software. We can handle everything</text>
        <text class="cover-copy" x="92" y="415">from installing practice management systems to imaging sensors, servers and</text>
        <text class="cover-copy" x="92" y="425">networks. Let us help plan your growth and keep your practice running smoothly.</text>
        <text class="cover-copy" x="92" y="435">We know teeth IT!</text>
      </g>
    </symbol>
  </defs>
</svg>

<svg class="sheet front-cover-sheet" viewBox="0 0 386 500" aria-label="Brochure front cover">
  <use href="#front-cover"/>
</svg>

<div class="open-spread" aria-label="Brochure open spread">
  <svg class="back-page" viewBox="0 0 300 388">
    <rect width="300" height="388" fill="var(--paper-grey)"/>
    <rect x="24" y="24" width="252" height="204" rx="8" fill="var(--white)"/>
    <rect x="150" y="24" width="126" height="14" rx="0" fill="var(--royal)"/>
    <text class="table-title" x="40" y="35">WHAT WE PROVIDE</text>
    <line x1="150" y1="38" x2="150" y2="228" stroke="#d3d5da" stroke-width=".8"/>

    <rect x="24" y="48" width="126" height="11" fill="var(--royal)"/>
    <text class="table-head" x="30" y="56">Network Setup</text>
    <text class="table-cell" x="30" y="69">Cabling and switches</text>
    <text class="table-cell" x="30" y="77">Wireless for staff</text>
    <text class="table-cell" x="30" y="85">Firewall installed</text>
    <text class="table-head" x="156" y="34">Data Backup</text>
    <text class="table-cell" x="156" y="50">Nightly image backup</text>
    <text class="table-cell" x="156" y="58">Offsite copies kept</text>
    <text class="table-cell" x="156" y="66">Tested restores</text>

    <rect x="24" y="100" width="252" height="11" fill="var(--royal)"/>
    <text class="table-head" x="30" y="108">Imaging Support</text>
    <text class="table-head" x="156" y="108">Security Audits</text>
    <text class="table-cell" x="30" y="121">Sensor installation</text>
    <text class="table-cell" x="30" y="129">Pano and CBCT</text>
    <text class="table-cell" x="30" y="137">Driver updates</text>
    <text class="table-cell" x="156" y="121">HIPAA risk review</text>
    <text class="table-cell" x="156" y="129">Password policy</text>
    <text class="table-cell" x="156" y="137">Patch management</text>

    <rect x="24" y="152" width="252" height="11" fill="var(--royal)"/>
    <text class="table-head" x="30" y="160">Help Desk</text>
    <text class="table-head" x="156" y="160">Remote Care</text>
    <text class="table-cell" x="30" y="173">Same day response</text>
    <text class="table-cell" x="30" y="181">Staff training</text>
    <text class="table-cell" x="30" y="189">Vendor calls handled</text>
    <text class="table-cell" x="156" y="173">Live monitoring</text>
    <text class="table-cell" x="156" y="181">Server health checks</text>
    <text class="table-cell" x="156" y="189">Monthly reports</text>

    <path d="M0 388 L0 300 L300 232 L300 388 Z" fill="url(#vault-tones)" role="img" aria-label="Photo of a heavy steel bank vault door set in stone"/>
    <path d="M150 388 L150 266 L300 232 L300 388 Z" fill="#1f2125" opacity=".92"/>
    <path d="M60 288 L300 232 L300 246 L60 302 Z" fill="var(--ribbon)"/>
    <text class="ribbon-text" x="86" y="292" transform="rotate(-12.8 86 292)">Secure cloud backup built for dental offices</text>
    <path d="M0 300 L60 288 L60 302 L0 314 Z" fill="var(--royal)"/>
    <text class="vault-heading" x="162" y="288">TOOTHSAFE.NET</text>
    <text class="vault-copy" x="162" y="306">Encrypted offsite backup for your</text>
    <text class="vault-copy" x="162" y="316">patient records and imaging files.</text>
    <text class="vault-copy" x="162" y="326">Restore fast after any failure.</text>
    <text class="vault-copy" x="162" y="336">Stay compliant and stay open.</text>
  </svg>
  <svg class="front-page" viewBox="0 0 386 500" preserveAspectRatio="none">
    <use href="#front-cover"/>
  </svg>
</div>

</body>
</html>
```